Promotional Postcard for Spring Cycling Camp in Utah

Need a promotional post card that will be distributed to bike shops to help encourage people to register for the event. The camp is both road and mountain biking near Redmesa Hollow National Park in Utah. The lodging is at a ranch. There will be professional cyclists to coach the riders and lead them on bicycle rides. It has to be a piece that will entice families and individuals. (This postcard will not be mailed)

Target Market(s)

avid cyclists - men and females
families of cyclists

Industry/Entity Type

Travel

Font styles to use
Serif

Colors
00a990
0555a3

Requirements
Must have
• pedal ridge outings logo
Nice to have
• photos of cycling, lodging
Should not have
• It is not a post card that will be mailed so no need for mailing area.

```html
<!DOCTYPE html>
<html lang="en">
<head>
<meta charset="utf-8">
<title>Spring Break Cycling Camp – Postcard</title>
<link rel="stylesheet" href="https://fonts.googleapis.com/css2?family=Oswald:wght@600;700&family=Questrial&display=swap">
<style>
  :root{
    --bg:#2b2b2d;
    --panel:rgba(22,26,32,.86);
    --ink:#ffffff;
    --accent-yellow:#f3f02a;
    --brand-teal:#00a990;
    --brand-blue:#0555a3;
    --sky:#5d9bd6;
    --rock:#b4582c;
    --sand:#d99a52;
    --wood:#b9732f;
    --pine:#3f6b3a;
  }
  *{box-sizing:border-box;margin:0;padding:0}
  html,body{width:1200px;height:900px;overflow:hidden;background:var(--bg)}
  body{font-family:"Questrial",sans-serif;color:var(--ink);position:relative}
  .card{position:absolute;top:250px;width:560px;height:380px;overflow:hidden;box-shadow:0 12px 30px rgba(0,0,0,.5)}
  .card--back{left:20px}
  .card--front{left:620px}
  .card svg.art{position:absolute;inset:0;width:100%;height:100%}

  /* back */
  .highlights{position:absolute;left:150px;top:40px;width:270px;text-align:center}
  .brand{display:flex;align-items:center;justify-content:center;gap:7px;margin-bottom:10px}
  .brand__mark{width:14px;height:14px;border-radius:50%;background:var(--brand-teal)}
  .brand__name{font-size:15px;color:var(--brand-teal);letter-spacing:.5px;text-transform:uppercase}
  .highlights__title{font-size:14px;letter-spacing:1.5px;text-transform:uppercase;margin-bottom:6px}
  .highlights__list{list-style:none;font-size:9.6px;line-height:1.32;color:var(--accent-yellow)}
  .highlights__list li::before{content:"• "}
  .more-info{margin-top:10px;font-size:10.5px;letter-spacing:.5px;text-transform:uppercase;line-height:1.35}

  /* front */
  .headline{position:absolute;left:150px;top:70px;width:270px;text-align:center}
  .headline__title{font-family:"Oswald",sans-serif;font-weight:700;color:var(--accent-yellow);font-size:42px;line-height:.98;text-transform:uppercase;letter-spacing:.5px}
  .headline__meta{display:flex;justify-content:center;align-items:flex-start;gap:14px;margin-top:12px}
  .headline__dates{font-size:17px;white-space:nowrap}
  .headline__place{font-size:12px;line-height:1.3;text-align:left}
  .tagline{position:absolute;left:0;right:0;bottom:14px;height:30px;background:var(--panel);color:var(--accent-yellow);font-size:14px;display:flex;align-items:center;justify-content:center}
</style>
</head>
<body>

<section class="card card--back" aria-label="Postcard back: highlights of the week">
  <svg class="art" viewBox="0 0 560 380" preserveAspectRatio="none">
    <polygon points="0,0 210,0 120,120 0,90" fill="var(--wood)" role="img" aria-label="Photo of a cozy ranch bedroom with a patchwork quilt"/>
    <polygon points="210,0 350,0 280,60" fill="var(--sky)" role="img" aria-label="Photo of a cyclist against blue sky"/>
    <polygon points="350,0 560,0 560,110 420,150" fill="#9c6a55" role="img" aria-label="Photo of a family relaxing together at the ranch"/>
    <polygon points="0,90 120,120 150,250 0,260" fill="#8a5a3a" role="img" aria-label="Photo of grilled ranch food"/>
    <polygon points="560,110 560,380 420,380 430,230" fill="#c8795a" role="img" aria-label="Photo of a ranch gate sign at sunset"/>
    <polygon points="0,260 150,250 260,380 0,380" fill="var(--pine)" role="img" aria-label="Photo of a log lodge with a teal roof and pine tree"/>
    <polygon points="150,250 430,230 420,380 260,380" fill="#6f6a5c" role="img" aria-label="Photo of the ranch grounds"/>
    <polygon points="120,120 210,0 350,0 420,150 430,230 420,340 150,340 140,230" fill="var(--panel)"/>
  </svg>
  <div class="highlights">
    <div class="brand"><span class="brand__mark"></span><span class="brand__name">Pedal Ridge Outings</span></div>
    <h2 class="highlights__title">Highlights of the week:</h2>
    <ul class="highlights__list">
      <li>Road Cycling &amp; Mountain Biking: Hone your road cycling and/or mountain biking skills or master some new techniques.</li>
      <li>Professional Cyclists to coach and lead you on the rides.</li>
      <li>Special rides for youth.</li>
      <li>Pro Tour Mechanics to care for your bicycle.</li>
      <li>Full Van Support for all rides.</li>
      <li>Hearty Ranch Food.</li>
      <li>Cozy &amp; Clean accommodations.</li>
      <li>Evening activities with the group or go off on your own and explore.</li>
    </ul>
    <p class="more-info">For more information<br>pedalridgeoutings.com</p>
  </div>
</section>

<section class="card card--front" aria-label="Postcard front: Spring Break Cycling Camp">
  <svg class="art" viewBox="0 0 560 380" preserveAspectRatio="none">
    <polygon points="0,0 300,0 150,70 0,60" fill="#c79a62" role="img" aria-label="Photo of desert scrub"/>
    <polygon points="300,0 560,0 560,110 420,60" fill="#8c8a80" role="img" aria-label="Photo of two road cyclists on a desert highway"/>
    <polygon points="420,60 560,110 560,280 430,200" fill="var(--rock)" role="img" aria-label="Photo of a mountain bike on red slickrock"/>
    <polygon points="0,60 150,70 150,190 0,200" fill="#a66440" role="img" aria-label="Photo of a mountain biker in red on a mesa trail"/>
    <polygon points="0,200 150,190 200,380 0,380" fill="#6b8fb8" role="img" aria-label="Photo of a smiling mountain biker under blue sky"/>
    <polygon points="150,190 290,220 330,380 200,380" fill="#7a94b4" role="img" aria-label="Low-angle photo of a bike fork and wheel"/>
    <polygon points="290,220 430,200 560,280 560,380 330,380" fill="var(--sand)" role="img" aria-label="Photo of a rider climbing a sandstone slope"/>
    <polygon points="150,70 300,0 420,60 430,200 290,220 150,190" fill="var(--panel)"/>
  </svg>
  <div class="headline">
    <h1 class="headline__title">Spring Break<br>Cycling Camp</h1>
    <div class="headline__meta">
      <p class="headline__dates">March 26 – April 1, 2017</p>
    </div>
    <div class="headline__meta">
      <p class="headline__place">Redmesa Hollow<br>Monticello, Utah</p>
    </div>
  </div>
  <p class="tagline">A great week of riding to kick the 2017 season off the right way!</p>
</section>

</body>
</html>
```